Postcard Design

Marlow Painting-all types of painting and staining-house,deck and roof powerwashing-stone and masonry sealing-
30 years in business-licensed and insured
Ray Pettibone
pettiboneworks@brushmail.example
9145820731

Industry/Entity Type

Painting

```html
<!DOCTYPE html>
<html lang="en">
<head>
<meta charset="utf-8">
<title>Marlow Painting Postcard</title>
<link rel="stylesheet" href="https://fonts.googleapis.com/css2?family=Orbitron:wght@500;700&family=Lato:wght@400&display=swap">
<style>
  :root {
    --page: #e9e9e9;
    --green-dark: #2f9b3c;
    --green-mid: #5dbb45;
    --green-light: #a6cf38;
    --roof: #5b3a93;
    --swoosh: #f4b21b;
    --photo-a: #c9343a;
    --photo-b: #d9a9a0;
    --blue: #1f3f9e;
    --ink: #24242e;
    --white: #ffffff;
    --tag: #f6d11b;
    --red: #e0242b;
    --rule: #555555;
  }
  * { margin: 0; padding: 0; box-sizing: border-box; }
  html, body { width: 900px; height: 1200px; overflow: hidden; }
  body { background: var(--page); position: relative; font-family: "Lato", sans-serif; }

  .card { position: absolute; left: 90px; width: 660px; overflow: hidden; box-shadow: 0 4px 14px rgba(0,0,0,.18); }
  .card svg.card-art { position: absolute; inset: 0; }
  .card-front { top: 70px; height: 510px; }
  .card-back { top: 620px; height: 525px; background: var(--white); }

  .heading { position: absolute; font-family: "Orbitron", sans-serif; font-weight: 700; white-space: nowrap; }
  .years { left: 78px; top: 392px; font-size: 41px; color: var(--blue); }
  .in-business { left: 78px; top: 436px; font-size: 32px; color: var(--ink); }
  .licensed { left: 79px; top: 475px; font-size: 16.5px; color: var(--white); font-weight: 500; }
  .brand-name { left: 368px; top: 442px; font-size: 20px; color: var(--white); font-weight: 700; }

  .offer-tag { position: absolute; left: 0; top: 77px; width: 225px; height: 51px; background: var(--tag); border-radius: 0 14px 14px 0; font-family: "Orbitron", sans-serif; font-weight: 700; font-size: 29px; color: var(--ink); padding: 7px 0 0 17px; white-space: nowrap; }
  .services { position: absolute; left: 40px; top: 163px; list-style: none; }
  .services li { font-size: 28px; color: var(--ink); height: 44.5px; padding-left: 34px; position: relative; }
  .services li::before { content: ""; position: absolute; left: 2px; top: 11px; width: 12px; height: 12px; border-radius: 50%; background: var(--red); }
  .contact-name { left: 16px; top: 374px; font-size: 23px; color: var(--white); }
  .contact-phone { left: 38px; top: 423px; font-size: 31px; color: var(--red); font-weight: 500; }
  .contact-email { left: 40px; top: 471px; font-size: 12px; color: var(--ink); }
</style>
</head>
<body>

<section class="card card-front">
  <svg class="card-art" width="660" height="510" viewBox="0 0 660 510">
    <defs>
      <linearGradient id="frontGreen" x1="0" y1="0" x2="1" y2="0">
        <stop offset="0" stop-color="var(--green-dark)"/>
        <stop offset="0.5" stop-color="var(--green-mid)"/>
        <stop offset="1" stop-color="var(--green-dark)"/>
      </linearGradient>
      <linearGradient id="photoTone" x1="0" y1="0" x2="1" y2="0">
        <stop offset="0" stop-color="var(--photo-a)"/>
        <stop offset="1" stop-color="var(--photo-b)"/>
      </linearGradient>
    </defs>
    <rect class="front-bg" width="660" height="510" fill="url(#frontGreen)"/>
    <polygon class="house-frame" points="0,180 330,36 660,175 660,380 0,385" fill="var(--white)"/>
    <polygon class="house-photo" role="img" aria-label="Photo: paint roller applying red paint to an interior wall" points="14,188 330,50 648,182 648,375 14,380" fill="url(#photoTone)"/>
    <rect class="chimney" x="130" y="55" width="50" height="60" fill="var(--roof)"/>
    <polyline class="roof-line" points="0,178 330,22 660,180" fill="none" stroke="var(--roof)" stroke-width="22" stroke-linejoin="miter"/>
    <path class="swoosh-white" d="M0,380 Q330,315 660,340 L660,372 Q330,335 0,400 Z" fill="var(--white)"/>
    <path class="swoosh-orange" d="M0,392 Q330,320 660,346 L660,358 Q330,336 0,402 Z" fill="var(--swoosh)"/>
    <path class="front-base" d="M0,402 Q330,336 660,358 L660,510 L0,510 Z" fill="url(#frontGreen)"/>
  </svg>
  <div class="heading years">30 YEARS</div>
  <div class="heading in-business">IN BUSINESS</div>
  <div class="heading licensed">LICENSED AND INSURED</div>
  <div class="heading brand-name">MARLOW PAINTING</div>
</section>

<section class="card card-back">
  <svg class="card-art" width="660" height="525" viewBox="0 0 660 525">
    <path class="accent-crescent" d="M330,0 Q420,230 305,525 L250,525 Q370,240 300,0 Z" fill="var(--red)"/>
    <path class="panel-edge" d="M0,0 L322,0 Q395,240 300,525 L0,525 Z" fill="var(--white)"/>
    <path class="offer-panel" d="M0,0 L312,0 Q385,240 292,525 L0,525 Z" fill="var(--green-light)"/>
    <rect class="stamp-box" x="555" y="113" width="60" height="64" fill="none" stroke="var(--rule)" stroke-width="1.2"/>
    <g class="address-lines" stroke="var(--rule)" stroke-width="1.2">
      <line x1="437" y1="248" x2="616" y2="248"/>
      <line x1="437" y1="278" x2="616" y2="278"/>
      <line x1="437" y1="310" x2="616" y2="310"/>
    </g>
  </svg>
  <div class="offer-tag">WE OFFER</div>
  <ul class="services">
    <li>Painting</li>
    <li>Staining</li>
    <li>Power washing</li>
    <li>Sealing</li>
  </ul>
  <div class="heading contact-name">RAY PETTIBONE</div>
  <div class="heading contact-phone">9145820731</div>
  <div class="heading contact-email">pettiboneworks@brushmail.example</div>
</section>

</body>
</html>
```